Lantern Hearthworks Business Cards

Looking to create simple business cards that highlight our unique three sided triangle fire pit design with the colors and font of our logo, listed below.

Requirements
Must have
• Looking for something simple that includes a picture of our fire pit with name, website (lanternhearthworks.com), phone number and email. Want to keep the color mostly orange and black.
• Font is gotham(medium) and orange color code is #ee6e22

```html
<!DOCTYPE html>
<html lang="en">
<head>
<meta charset="utf-8">
<title>Lantern Hearthworks Business Cards</title>
<link href="https://fonts.googleapis.com/css2?family=Montserrat:wght@400;500;600&display=swap" rel="stylesheet">
<style>
  :root {
    --ink: #262425;
    --ink-deep: #1c1b1c;
    --flame: #ee6e22;
    --paper: #ffffff;
    --mist: #e6e6e6;
    --mist-dark: #cfcfcf;
    --backdrop: #8a6a45;
  }
  * { box-sizing: border-box; margin: 0; padding: 0; }
  html, body { width: 1200px; height: 939px; overflow: hidden; }
  body {
    background: var(--backdrop);
    font-family: "Montserrat", sans-serif;
    position: relative;
  }
  .card {
    position: absolute;
    width: 560px;
    height: 320px;
    border-radius: 26px;
    overflow: hidden;
    box-shadow: 0 14px 30px rgba(0,0,0,.45);
  }
  .card-front {
    left: 50px; top: 110px;
    background: var(--ink);
    display: flex; align-items: center; justify-content: center;
  }
  .card-back {
    left: 590px; top: 510px;
    background: var(--paper);
  }
  .wordmark {
    display: flex; align-items: center; gap: 22px;
  }
  .wordmark-dot {
    width: 46px; height: 46px; border-radius: 50%;
    background: var(--flame);
    flex: none;
  }
  .wordmark-name {
    color: var(--paper);
    font-weight: 500;
    text-transform: uppercase;
    letter-spacing: .22em;
    line-height: 1.15;
    font-size: 30px;
  }
  .back-brand {
    position: absolute; left: 0; top: 0; bottom: 0; width: 300px;
    background: var(--ink);
    display: flex; align-items: center; justify-content: center;
  }
  .back-brand .wordmark { gap: 14px; }
  .back-brand .wordmark-dot { width: 30px; height: 30px; }
  .back-brand .wordmark-name { font-size: 19px; }
  .identity {
    position: absolute; left: 300px; right: 0; top: 0; height: 100px;
    padding: 26px 30px 0 0; text-align: right;
  }
  .identity-name {
    color: var(--flame); font-weight: 600; font-size: 24px;
  }
  .identity-role {
    color: var(--flame); font-weight: 400; font-size: 16px; margin-top: 2px;
  }
  .contact-panel {
    position: absolute; left: 300px; right: 0; top: 108px; height: 150px;
    background: var(--mist);
    border-left: 22px solid var(--mist-dark);
    padding: 18px 0 0 26px;
    list-style: none;
  }
  .contact-item {
    display: flex; align-items: center; gap: 10px;
    color: var(--flame); font-size: 15px; line-height: 30px;
  }
  .contact-item svg { width: 14px; height: 14px; fill: var(--ink); flex: none; }
</style>
</head>
<body>

<section class="card card-front" aria-label="Card front">
  <div class="wordmark">
    <span class="wordmark-dot"></span>
    <span class="wordmark-name">Lantern<br>Hearthworks</span>
  </div>
</section>

<section class="card card-back" aria-label="Card back">
  <div class="back-brand">
    <div class="wordmark">
      <span class="wordmark-dot"></span>
      <span class="wordmark-name">Lantern<br>Hearthworks</span>
    </div>
  </div>
  <div class="identity">
    <p class="identity-name">Owen Marsh</p>
    <p class="identity-role">Founder/CEO</p>
  </div>
  <ul class="contact-panel">
    <li class="contact-item">
      <svg viewBox="0 0 16 16"><path d="M1 3h14v10H1z M1 3l7 6 7-6" fill="none" stroke="#262425" stroke-width="1.6"/></svg>
      lanternhearthworks.com
    </li>
    <li class="contact-item">
      <svg viewBox="0 0 16 16"><path d="M4 1l3 3-2 2c1 2 3 4 5 5l2-2 3 3-2 3C7 15 1 9 1 4z"/></svg>
      503-555-0142
    </li>
    <li class="contact-item">
      <svg viewBox="0 0 16 16"><path d="M1 6c0-3 14-3 14 0v1h-4V5H5v2H1z M3 8h10l2 6H1z"/></svg>
      503-555-0187
    </li>
    <li class="contact-item">
      <svg viewBox="0 0 16 16"><path d="M1 2h14v10H1z M3 4v6h10V4z M5 13h6v2H5z"/></svg>
      lanternhearthworks.com
    </li>
  </ul>
</section>

</body>
</html>
```